Flyer for the Harvest Lantern Gathering 2018

Design a flyer for our annual conference with basic information about the conference: conference logo and year,

Location:
Tolvane Community Center (Downtown Portland)
482 Wexmoor Street, Portland, ME 04107,

Date:
August 24th, 25th and 26th, 2018
Start time 6:00PM

I would like the following three words added to the flyer. These words describe the vision of the conference:
Prophetic, Worship, Prayer

```html
<!DOCTYPE html>
<html lang="en">
<head>
<meta charset="utf-8">
<title>Harvest Lantern Gathering 2018 – Annual Conference</title>
<link href="https://fonts.googleapis.com/css2?family=Inter+Tight:wght@600;700&family=Archivo:wght@700&display=swap" rel="stylesheet">
<style>
  :root {
    --page: #ffffff;
    --stone: #c8c6c7;
    --gold-light: #f0d35c;
    --gold-deep: #e6b424;
    --ink: #111111;
    --ember: #e09a1c;
    --photo-dark: #0c0b10;
    --photo-teal: #2f9c9c;
  }
  html, body {
    margin: 0;
    padding: 0;
    width: 1200px;
    height: 1200px;
    overflow: hidden;
    background: var(--page);
  }
  .flyer {
    position: absolute;
    left: 177.6px;
    top: 0;
    width: 844.8px;
    height: 1200px;
  }
  .flyer svg {
    position: absolute;
    inset: 0;
    width: 100%;
    height: 100%;
  }
  .banner-title {
    font-family: "Archivo", Arial, sans-serif;
    font-weight: 700;
    font-size: 66px;
    fill: var(--ink);
  }
  .brand-name {
    font-family: "Inter Tight", Arial, sans-serif;
    font-weight: 600;
    font-size: 34px;
    letter-spacing: 3px;
    fill: #2a2a2a;
  }
  .vision {
    font-family: "Inter Tight", Arial, sans-serif;
    font-weight: 700;
    font-size: 80px;
    letter-spacing: -3px;
    fill: var(--ink);
  }
  .details {
    font-family: "Inter Tight", Arial, sans-serif;
    font-weight: 600;
    font-size: 42px;
    letter-spacing: -1.6px;
    fill: var(--ink);
  }
</style>
</head>
<body>
  <div class="flyer">
    <svg class="flyer-background" viewBox="222 0 1056 1500" preserveAspectRatio="none" aria-hidden="true">
      <defs>
        <linearGradient id="gold-wash" x1="0" y1="0" x2="0" y2="1">
          <stop offset="0" stop-color="var(--gold-light)"/>
          <stop offset="1" stop-color="var(--gold-deep)"/>
        </linearGradient>
        <linearGradient id="ember-ring" x1="0" y1="0" x2="0" y2="1">
          <stop offset="0" stop-color="#f0c040"/>
          <stop offset="1" stop-color="#d88a14"/>
        </linearGradient>
      </defs>
      <rect class="page-stone" x="222" y="0" width="1056" height="1500" fill="var(--stone)"/>
      <polygon class="top-band" points="222,275 985,0 1278,0 1278,95 222,330" fill="url(#gold-wash)"/>
      <polygon class="lower-panel" points="222,830 1278,765 1278,1432 840,1500 222,1500" fill="url(#gold-wash)"/>

      <circle class="brand-mark" cx="375" cy="75" r="64" fill="none" stroke="url(#ember-ring)" stroke-width="3"/>
      <text class="brand-name" x="375" y="175" text-anchor="middle">HLGCON</text>

      <text class="banner-title" x="560" y="226" transform="rotate(-12.4 560 226)" textLength="690" lengthAdjust="spacingAndGlyphs">ANNUAL CONFERENCE</text>

      <text class="vision" x="750" y="925" text-anchor="middle">Prophetic. Worship. Prayer.</text>

      <text class="details" x="747" y="1038" text-anchor="middle">Location:</text>
      <text class="details" x="746" y="1098" text-anchor="middle">Tolvane Community Center (Downtown Portland)</text>
      <text class="details" x="746" y="1158" text-anchor="middle">482 Wexmoor Street, Portland, ME 04107,</text>

      <text class="details" x="705" y="1300" text-anchor="middle">Date:</text>
      <text class="details" x="705" y="1360" text-anchor="middle">August 24th, 25th and 26th, 2018</text>
      <text class="details" x="707" y="1420" text-anchor="middle">Start time 6:00PM</text>
    </svg>

    <svg class="worship-photo" viewBox="222 0 1056 1500" preserveAspectRatio="none" role="img" aria-label="Photo of a worship crowd in a dark hall with hands raised, lit in teal">
      <defs>
        <linearGradient id="crowd-tone" x1="0" y1="0" x2="0" y2="1">
          <stop offset="0" stop-color="var(--photo-dark)"/>
          <stop offset="0.45" stop-color="#17262a"/>
          <stop offset="1" stop-color="var(--photo-teal)"/>
        </linearGradient>
      </defs>
      <polygon points="222,330 1278,95 1278,655 222,810" fill="url(#crowd-tone)"/>
    </svg>
  </div>
</body>
</html>
```